Nice concept website for free living

A website for promoting 2 concepts.

---
Live for free in amsterdam -

homeowner? --- or --- searching to rent?

HOMEOWNER PAGE:

instructions on one page --- homeowners can make x amount in a legal way - and click for more information. Form or contact direct by mobile number.

SEARCHING TO RENT PAGE:

First fill out their details quick form --- Available properties --- show available properties.

Target Market(s)

1. People needing a place to live
2. Homeowners that want more revenue from their real estate

Industry/Entity Type

Tourism

Number of Pages Required

3 page

Requirements
Must have
• Simple nice design
• Homepage quick explanation - what is the concept and choice for
• 1. Homeowners
• 2. Renters
Nice to have
• fresh design

```html
<!DOCTYPE html>
<html lang="en">
<head>
<meta charset="utf-8">
<title>Canalnest – A Free Living in Netherlands</title>
<link rel="stylesheet" href="https://fonts.googleapis.com/css2?family=Raleway:wght@500;700;800&family=Open+Sans:wght@400;600&display=swap">
<style>
  :root {
    --purple: #8a3fc0;
    --magenta: #c8259f;
    --blue: #3f7fd0;
    --nav-text: #333438;
    --white: #ffffff;
    --footer-bg: #4a4b50;
    --photo-dark: #3c4a5c;
    --photo-mid: #8e9aa6;
    --photo-light: #d9dde0;
  }
  * { margin: 0; padding: 0; box-sizing: border-box; }
  html, body { width: 1200px; height: 755px; overflow: hidden; background: var(--white); }
  body { font-family: "Open Sans", Arial, sans-serif; position: relative; }

  .site-header {
    position: absolute; left: 0; top: 0; width: 1200px; height: 125px;
    background: var(--white); border-top: 3px solid var(--purple);
  }
  .brand {
    position: absolute; left: 102px; top: 56px;
    display: flex; align-items: center; gap: 10px;
    font-family: "Open Sans", Arial, sans-serif; font-weight: 400;
    font-size: 25px; color: var(--nav-text); letter-spacing: 0.5px;
  }
  .brand-dot { width: 14px; height: 14px; border-radius: 50%; background: var(--purple); }
  .phone {
    position: absolute; left: 974px; top: 26px;
    display: flex; align-items: center; gap: 7px;
    font-size: 13px; color: var(--nav-text);
  }
  .main-nav {
    position: absolute; top: 75px; left: 0;
    font-family: "Raleway", Arial, sans-serif; font-weight: 500; font-size: 12px;
    letter-spacing: 0.4px; color: var(--nav-text);
  }
  .main-nav a { position: absolute; white-space: nowrap; color: inherit; text-decoration: none; }
  .main-nav a.active { color: var(--blue); }
  .nav-underline { position: absolute; left: 604px; top: 92px; }
  .search-icon { position: absolute; left: 1086px; top: 75px; }

  .hero {
    position: absolute; left: 0; top: 125px; width: 1200px; height: 630px;
    background: linear-gradient(100deg, var(--photo-light) 0%, var(--photo-mid) 30%, var(--photo-dark) 48%, var(--photo-mid) 70%, #b7c0b8 100%);
  }
  .hero-copy { position: absolute; left: 688px; top: 217px; color: var(--white); }
  .hero-kicker { font-family: "Raleway", Arial, sans-serif; font-weight: 500; font-size: 13px; letter-spacing: 0.2px; }
  .hero-title { font-family: "Raleway", Arial, sans-serif; font-weight: 800; font-size: 26px; margin-top: 6px; letter-spacing: 0.3px; }
  .hero-points { list-style: none; margin-top: 12px; font-size: 12.5px; }
  .hero-points li { display: flex; align-items: center; gap: 9px; height: 27.5px; padding-left: 3px; }
  .hero-actions { display: flex; align-items: center; margin-top: 9px; }
  .btn {
    width: 143px; height: 44px; border-radius: 22px; display: flex; align-items: center; justify-content: center;
    color: var(--white); font-size: 12px;
  }
  .btn-owner { background: linear-gradient(180deg, #d23fae, #a81f8a); }
  .btn-renter { background: linear-gradient(180deg, #5a8fd0, #3c6aa8); }
  .or { width: 38px; text-align: center; font-size: 12px; font-weight: 600; }
  .slider-arrow { position: absolute; top: 349px; }

  .site-footer { position: absolute; left: 0; top: 0; width: 1200px; height: 755px; pointer-events: none; }
  .footer-links { position: absolute; left: 100px; top: 687px; color: var(--white); font-size: 13px; }
  .footer-links span.sep { margin: 0 13px; }
  .copyright { position: absolute; left: 100px; top: 714px; color: var(--white); font-size: 13px; }
  .social { position: absolute; left: 951px; top: 688px; display: flex; gap: 4px; }
  .social span { width: 35px; height: 35px; border-radius: 50%; border: 2px solid rgba(255,255,255,0.35); }
</style>
</head>
<body>
  <header class="site-header">
    <div class="brand"><span class="brand-dot"></span>Canalnest</div>
    <div class="phone">
      <svg width="24" height="24" viewBox="0 0 24 24"><circle cx="12" cy="12" r="11" fill="none" stroke="#2a8fd6" stroke-width="1.6"/><path d="M8.5 7c.6-.4 1.2 0 1.5.6l.7 1.5c.2.5 0 1-.4 1.3l-.6.5c.6 1.3 1.6 2.3 2.9 2.9l.5-.6c.3-.4.8-.6 1.3-.4l1.5.7c.6.3 1 .9.6 1.5-.6 1-1.6 1.5-2.7 1.2-3-.9-5.3-3.2-6.2-6.2-.3-1.1.2-2.1 1.2-2.7z" fill="#2a8fd6"/></svg>
      +31 20 555 0147
    </div>
    <nav class="main-nav">
      <a class="active" href="#" style="left:613px">HOME</a>
      <a href="#" style="left:690px">ABOUT US</a>
      <a href="#" style="left:793px">SERVICES</a>
      <a href="#" style="left:894px">TEAM</a>
      <a href="#" style="left:972px">CONTACT US</a>
    </nav>
    <svg class="nav-underline" width="66" height="12" viewBox="0 0 66 12"><defs><linearGradient id="ul" x1="0" x2="1"><stop offset="0" stop-color="#c8259f"/><stop offset="1" stop-color="#3f7fd0"/></linearGradient></defs><path d="M1 10 C8 1 30 2 65 6" fill="none" stroke="url(#ul)" stroke-width="2.2" stroke-linecap="round"/></svg>
    <svg class="search-icon" width="14" height="14" viewBox="0 0 14 14"><circle cx="5.8" cy="5.8" r="4.3" fill="none" stroke="#333438" stroke-width="2"/><path d="M9 9l3.8 3.8" stroke="#333438" stroke-width="2.2" stroke-linecap="round"/></svg>
  </header>

  <main class="hero" role="img" aria-label="Photo of a couple embracing, seen from behind, looking at a modern white apartment building">
  </main>

  <svg class="slider-arrow" style="left:36px" width="18" height="54" viewBox="0 0 18 54"><path d="M17 1 L1 27 L17 53" fill="none" stroke="#fff" stroke-width="1.3"/></svg>
  <svg class="slider-arrow" style="left:1144px" width="18" height="54" viewBox="0 0 18 54"><path d="M1 1 L17 27 L1 53" fill="none" stroke="#fff" stroke-width="1.3"/></svg>

  <section class="hero-copy">
    <p class="hero-kicker">HOMEOWNERS CAN MAKE X AMOUNT IN A LEGAL WAY</p>
    <h1 class="hero-title">A FREE LIVING IN NETHERLANDS</h1>
    <ul class="hero-points">
      <li><svg width="11" height="9" viewBox="0 0 11 9"><path d="M1 4.5l3 3L10 1.5" fill="none" stroke="#fff" stroke-width="2"/></svg>Lorem Ipsum is simply dummy text of the printing</li>
      <li><svg width="11" height="9" viewBox="0 0 11 9"><path d="M1 4.5l3 3L10 1.5" fill="none" stroke="#fff" stroke-width="2"/></svg>Contrary to popular belief, Lorem Ipsum</li>
      <li><svg width="11" height="9" viewBox="0 0 11 9"><path d="M1 4.5l3 3L10 1.5" fill="none" stroke="#fff" stroke-width="2"/></svg>Finibus Bonorum et Malorum</li>
    </ul>
    <div class="hero-actions">
      <span class="btn btn-owner">Home owner</span>
      <span class="or">OR</span>
      <span class="btn btn-renter">Searching to rent</span>
    </div>
  </section>

  <footer>
    <svg class="site-footer" viewBox="0 0 1200 755">
      <defs>
        <linearGradient id="wave" x1="0" x2="1">
          <stop offset="0" stop-color="#d21f9c"/>
          <stop offset="0.45" stop-color="#9b44c0"/>
          <stop offset="1" stop-color="#4f6fd0"/>
        </linearGradient>
      </defs>
      <path d="M0 668 C120 630 300 620 420 628 C650 645 900 680 1050 668 C1120 662 1170 652 1200 645 L1200 755 L0 755 Z" fill="url(#wave)"/>
      <path d="M0 717 C120 670 300 652 440 660 C650 672 880 682 1050 672 C1120 667 1170 658 1200 650 L1200 755 L0 755 Z" fill="#4a4b50"/>
    </svg>
    <p class="footer-links">Terms and conditions<span class="sep">/</span>Privacy policy<span class="sep">/</span>Help</p>
    <p class="copyright">Copyright 2016&nbsp; Canalnest. All Rights Reserved</p>
    <div class="social">
      <span style="background:#3f5fa8"></span>
      <span style="background:#2fa6e4"></span>
      <span style="background:#2a77a8"></span>
      <span style="background:#d0483e"></span>
    </div>
  </footer>
</body>
</html>
```